We need a business card and letterhead design for an orthodontic office. Needs to be clean, simple and sleek

Target Market(s)

adults/children

Industry/Entity Type

Dental

Contact Information for Business Card

Logo that is attached

Font styles to use
Serif

Colors

Designer to choose colors to be used in the design.

Requirements
Must have
• Peter L Vantrell DDS
• Corinne Palk DMD
• 82 Tolland Avenue
• Merrick,NY 11903
• (516) 742-5096
• www.vantrellortho.example
Nice to have
• on the back.... space for appointment times
Should not have
• teeth

```html
<!DOCTYPE html>
<html lang="en">
<head>
<meta charset="utf-8">
<title>Vantrell Orthodontics – Business Card</title>
<link rel="stylesheet" href="https://fonts.googleapis.com/css2?family=Lato:wght@300;400;700;900&display=swap">
<style>
  :root {
    --page-bg: #e9ecef;
    --card-edge: #58aee0;
    --panel-top: #3f8fc0;
    --panel-bottom: #5fb2e2;
    --panel-front-top: #2f6f98;
    --panel-front-bottom: #3f8bbb;
    --bar-dark: #262729;
    --bar-grey: #4a4b4e;
    --text-light: #ffffff;
    --text-soft: rgba(255,255,255,0.82);
    --text-deep: #1d3447;
  }
  * { margin: 0; padding: 0; box-sizing: border-box; }
  html, body {
    width: 1200px; height: 800px; overflow: hidden;
    background: var(--page-bg);
    font-family: "Lato", Arial, sans-serif;
  }
  .sheet {
    width: 1200px; height: 800px;
    display: flex; align-items: center; justify-content: center; gap: 48px;
  }
  .card {
    position: relative;
    width: 540px; height: 309px;
    background: var(--card-edge);
    box-shadow: 0 10px 28px rgba(0,0,0,0.18);
    overflow: hidden;
  }
  .card__panel {
    position: absolute; inset: 18px;
  }

  /* Front */
  .card--front .card__panel {
    background: linear-gradient(160deg, var(--panel-front-top), var(--panel-front-bottom));
  }
  .brand {
    position: absolute; left: 52px; top: 40px;
    color: var(--text-soft); text-transform: uppercase;
    font-weight: 300; line-height: 0.98; letter-spacing: 2px;
  }
  .brand__line { display: block; font-size: 50px; }
  .brand__sub { display: block; font-size: 30px; letter-spacing: 3px; margin-top: 4px; color: rgba(255,255,255,0.7); }
  .hours-bar {
    position: absolute; left: 0; right: 0; bottom: 14px; height: 40px;
    background: var(--bar-dark);
    display: flex; align-items: center; justify-content: center; gap: 10px;
    color: var(--text-light); font-size: 13px; font-weight: 700; letter-spacing: 0.5px;
  }

  /* Back */
  .card--back .card__panel {
    background: linear-gradient(200deg, var(--panel-top), var(--panel-bottom));
  }
  .doctor {
    position: absolute; text-transform: uppercase; line-height: 1;
  }
  .doctor__name { display: block; color: var(--text-light); font-weight: 900; font-size: 23px; letter-spacing: 0.5px; }
  .doctor__title { display: block; color: var(--text-deep); font-weight: 700; font-size: 19px; margin-top: 3px; }
  .doctor--primary { left: 22px; top: 120px; }
  .doctor--partner { right: 20px; top: 20px; text-align: right; }
  .info-bar {
    position: absolute; height: 30px;
    display: flex; align-items: center; gap: 12px; padding-left: 10px;
    color: var(--text-light); font-size: 13px; font-weight: 700;
  }
  .info-bar--phone { left: 0; top: 200px; width: 292px; background: var(--bar-dark); }
  .info-bar--address { left: 26px; top: 236px; width: 336px; background: var(--bar-grey); }
  .info-bar--web { left: 300px; top: 150px; width: 190px; background: var(--bar-grey); font-size: 12px; }
  .accent-strip { position: absolute; left: 496px; top: 150px; width: 8px; height: 52px; background: var(--bar-grey); opacity: 0.8; }
  .icon { width: 15px; height: 15px; flex: none; }
</style>
</head>
<body>
<main class="sheet">
  <section class="card card--front" aria-label="Card front">
    <div class="card__panel">
      <h1 class="brand">
        <span class="brand__line">Peter</span>
        <span class="brand__line">Vantrell</span>
        <span class="brand__sub">Orthodontics</span>
      </h1>
      <div class="hours-bar">
        <svg class="icon" viewBox="0 0 16 16" aria-hidden="true"><circle cx="8" cy="8" r="6.5" fill="none" stroke="#fff" stroke-width="1.6"/><path d="M8 4.2V8h3" fill="none" stroke="#fff" stroke-width="1.6" stroke-linecap="round"/></svg>
        <span>10 AM to 6 PM</span>
      </div>
    </div>
  </section>

  <section class="card card--back" aria-label="Card back">
    <div class="card__panel">
      <div class="doctor doctor--partner">
        <span class="doctor__name">Corinne Palk</span>
        <span class="doctor__title">DMD</span>
      </div>
      <div class="doctor doctor--primary">
        <span class="doctor__name">Peter L Vantrell</span>
        <span class="doctor__title">DDS</span>
      </div>
      <div class="info-bar info-bar--web">
        <svg class="icon" viewBox="0 0 16 16" aria-hidden="true"><circle cx="8" cy="8" r="6.5" fill="none" stroke="#fff" stroke-width="1.3"/><path d="M1.5 8h13M8 1.5c-3 3.5-3 9.5 0 13M8 1.5c3 3.5 3 9.5 0 13M2.8 4.8h10.4M2.8 11.2h10.4" fill="none" stroke="#fff" stroke-width="1"/></svg>
        <span>www.vantrellortho.example</span>
      </div>
      <div class="accent-strip"></div>
      <div class="info-bar info-bar--phone">
        <svg class="icon" viewBox="0 0 16 16" aria-hidden="true"><path d="M4.5 1.8 6.4 4.6 5 6.2c.8 1.8 2.2 3.3 4 4.1l1.5-1.4 2.8 1.9-.9 2.6C7.3 13.2 2.8 8.7 1.9 3z" fill="#fff"/></svg>
        <span>(516) 742-5096</span>
      </div>
      <div class="info-bar info-bar--address">
        <svg class="icon" viewBox="0 0 16 16" aria-hidden="true"><path d="M8 15s5-5.2 5-8.8A5 5 0 0 0 3 6.2C3 9.8 8 15 8 15z" fill="#fff"/><circle cx="8" cy="6.2" r="1.9" fill="#4a4b4e"/></svg>
        <span>82 Tolland Avenue Merrick,NY 11903</span>
      </div>
    </div>
  </section>
</main>
</body>
</html>
```